Anzeigengestaltung für KFZ-Werkstatt
Zielgruppe
Wir sind eine KFZ-Werkstatt mit vielumfänglichen Dienstleistungen. Unsere Zielgruppe beschränkt sich auf einen Umkreis von ca. 10km. Wir bieten alles rund ums KFZ: Service, Inspektion, Reparaturen aller Art, TÜV, Rad/Reifen/Felgen, Spurvermessung, Unfallinstandsetzung.
Aufgabenstellung
wir nutzen den Hashtag '#wagenhofmoosl' für Werbung im Internet sowie in den Werbeanzeigen. Wir verwenden diesen 'Slogan' in der SChriftart 'Hashtag', diese kann überall runtergeladen werden. dieser muss in den Werbeanzeigen nicht im Vordergrund stehen, da hier die Zielgruppe eher in Richtung 40+ geht.
es muss auch Platz für die offizielle Firmierung samt Anschrift, Telefon und Internet sein (kein Fax).
was die Anzeige an sich angeht, so sollte das Motiv (gerne erst mal einfach ein Stockfoto) durch uns austauschbar sein. Sprich: wenn Reifensaison ist, wollen wir da ein eigenes Motiv reinstecken können; im Sommer wiederum ein anderes etc. Zudem verwenden wir auch Standardfotos von unserem Unternehmen, welches wir platzieren lassen wenn ein Monat mal nichts besonderes ansteht (die Werbung wird monatlich geschaltet).
Maße: 172x100mm
Hauptfarben (bedingt durch das System, an das wir angeschlossen sind):
ROT: C15 M100 Y100 K0 (oder HKS15; oder Pantone 1797)
GRAU: C0 M0 Y0 K50 (oder 50% HKS90; oder Pantone Cool Gray 7)
Aufgrund der Zielgruppe haben wir als Wunsch 'erschwinglich' angegeben. Dies soll aber nicht heißen, dass wir nicht bereit sind, für das Erstellen der Anzeige kein Geld auszugeben. Nein, damit wollen wir unterstreichen, dass es nicht irre aufgepusht sein soll mit wahnsinns-Effekten etc.

```html
<!DOCTYPE html>
<html lang="de">
<head>
<meta charset="utf-8">
<title>Wagenhof Moosl – Anzeige</title>
<link href="https://fonts.googleapis.com/css2?family=Roboto+Condensed:wght@400;700&family=Caveat:wght@500&display=swap" rel="stylesheet">
<style>
  :root {
    --red: #d8282c;
    --red-deep: #c81f24;
    --grey: #9d9d9d;
    --page: #eeeeee;
    --white: #ffffff;
    --photo-dark: #3a3f48;
    --photo-red: #d9463a;
    --badge-blue: #1f4f9a;
  }
  * { margin: 0; padding: 0; box-sizing: border-box; }
  html, body { width: 1200px; height: 1200px; overflow: hidden; background: var(--page); }
  body { position: relative; font-family: "Roboto Condensed", sans-serif; }

  .ad {
    position: absolute; left: 123px; top: 303px; width: 966px; height: 562px;
    background: var(--white); overflow: hidden;
    box-shadow: 0 2px 8px rgba(0,0,0,0.12);
  }
  .brand {
    position: absolute; left: 28px; top: 44px;
    display: flex; align-items: center; gap: 8px;
    font-weight: 700; font-size: 22px; color: var(--red); letter-spacing: 0.5px;
  }
  .brand-dot { width: 14px; height: 14px; border-radius: 50%; background: var(--red); }

  .booking { position: absolute; left: 292px; top: 27px; display: flex; gap: 20px; align-items: center; }
  .booking-label { font-weight: 700; font-size: 14px; color: var(--red); line-height: 1; }
  .booking-number { font-weight: 700; font-size: 44px; color: var(--red); line-height: 1; margin-top: 2px; letter-spacing: 0.5px; }

  .motif {
    position: absolute; left: 0; top: 95px; width: 662px; height: 412px;
    background: linear-gradient(100deg, var(--photo-dark) 0%, #5b5f66 40%, var(--photo-red) 75%, #e25a4c 100%);
  }
  .motif-edge {
    position: absolute; left: 945px; top: 95px; width: 21px; height: 412px;
    background: linear-gradient(180deg, #5a6070, #3c4250);
  }

  .service-panel {
    position: absolute; left: 662px; top: 0; width: 283px; height: 562px;
    background: var(--red); color: var(--white);
  }
  .service-title {
    text-align: center; font-weight: 700; font-size: 31px; line-height: 35px;
    margin-top: 33px; letter-spacing: 0.5px;
  }
  .service-rule { margin: 13px 20px 0; height: 1px; background: rgba(255,255,255,0.8); }
  .service-list { list-style: none; margin: 26px 0 0 32px; }
  .service-list li { display: flex; align-items: center; gap: 14px; font-size: 23px; height: 36px; }
  .service-list svg { width: 17px; height: 14px; flex: none; }

  .badges { position: absolute; left: 68px; top: 408px; display: flex; align-items: flex-end; gap: 26px; }
  .badge-round { width: 64px; height: 64px; border-radius: 50%; background: var(--badge-blue); border: 3px solid var(--white); }
  .badge-shield { width: 58px; height: 86px; border-radius: 29px 29px 3px 3px; background: var(--badge-blue); }

  .hashtag {
    position: absolute; left: 0; bottom: 8px; width: 100%; text-align: center;
    font-family: "Caveat", cursive; font-size: 34px; color: var(--white);
  }

  .contact-bar {
    position: absolute; left: 0; top: 507px; width: 662px; height: 55px;
    background: var(--grey); color: var(--white);
    display: flex; align-items: center; font-weight: 700; font-size: 19px;
  }
  .contact-bar .edge { position: absolute; }
  .contact-item { display: flex; align-items: center; gap: 12px; }
  .contact-address { margin-left: 27px; }
  .contact-mail { margin-left: 52px; }
  .grey-edge { position: absolute; left: 945px; top: 507px; width: 21px; height: 55px; background: var(--grey); }
</style>
</head>
<body>
  <div class="ad">
    <div class="brand"><span class="brand-dot"></span>WAGENHOF MOOSL</div>

    <div class="booking">
      <svg width="26" height="50" viewBox="0 0 26 50" aria-hidden="true">
        <rect x="2" y="8" width="20" height="38" rx="3" fill="none" stroke="#d8282c" stroke-width="3"/>
        <rect x="6" y="13" width="12" height="24" fill="#d8282c"/>
        <circle cx="12" cy="41" r="1.8" fill="#d8282c"/>
        <path d="M19 2 a6 6 0 0 1 5 5 M18 5 a3 3 0 0 1 3 3" fill="none" stroke="#d8282c" stroke-width="1.6"/>
      </svg>
      <div>
        <div class="booking-label">Terminvereinbarung unter:</div>
        <div class="booking-number">09471-3582</div>
      </div>
    </div>

    <div class="motif" role="img" aria-label="Foto: Mechaniker in roter Arbeitskleidung montiert ein Rad an einem Auto"></div>
    <div class="motif-edge"></div>

    <div class="contact-bar">
      <div class="contact-item contact-address">
        <svg width="22" height="28" viewBox="0 0 22 28" aria-hidden="true">
          <path d="M11 1 C5 1 1 5.5 1 11 C1 18 11 27 11 27 C11 27 21 18 21 11 C21 5.5 17 1 11 1 Z" fill="#fff"/>
          <circle cx="11" cy="11" r="4" fill="#9d9d9d"/>
        </svg>
        Talweg 12 | 93199 Moosl
      </div>
      <div class="contact-item contact-mail">
        <svg width="34" height="22" viewBox="0 0 34 22" aria-hidden="true">
          <rect x="1" y="1" width="32" height="20" fill="none" stroke="#fff" stroke-width="2"/>
          <path d="M1 1 L17 13 L33 1 M1 21 L13 10 M33 21 L21 10" fill="none" stroke="#fff" stroke-width="2"/>
        </svg>
        info@wagenhof-moosl.de
      </div>
    </div>
    <div class="grey-edge"></div>

    <div class="service-panel">
      <h2 class="service-title">KFZ<br>RUNDUM SERVICE</h2>
      <div class="service-rule"></div>
      <ul class="service-list">
        <li><svg viewBox="0 0 17 14"><path d="M1 7 L6 12 L16 1" fill="none" stroke="#fff" stroke-width="2"/></svg>Inspektion</li>
        <li><svg viewBox="0 0 17 14"><path d="M1 7 L6 12 L16 1" fill="none" stroke="#fff" stroke-width="2"/></svg>Reparaturen aller Art</li>
        <li><svg viewBox="0 0 17 14"><path d="M1 7 L6 12 L16 1" fill="none" stroke="#fff" stroke-width="2"/></svg>TÜV / HU</li>
        <li><svg viewBox="0 0 17 14"><path d="M1 7 L6 12 L16 1" fill="none" stroke="#fff" stroke-width="2"/></svg>Rad/Reifen/Felgen</li>
        <li><svg viewBox="0 0 17 14"><path d="M1 7 L6 12 L16 1" fill="none" stroke="#fff" stroke-width="2"/></svg>Spurvermessung</li>
        <li><svg viewBox="0 0 17 14"><path d="M1 7 L6 12 L16 1" fill="none" stroke="#fff" stroke-width="2"/></svg>Unfallinstandsetzung</li>
        <li><svg viewBox="0 0 17 14"><path d="M1 7 L6 12 L16 1" fill="none" stroke="#fff" stroke-width="2"/></svg>und vieles mehr</li>
      </ul>
      <div class="badges">
        <div class="badge-round"></div>
        <div class="badge-shield"></div>
      </div>
      <div class="hashtag">#wagenhofmoosl</div>
    </div>
  </div>
</body>
</html>
```